TKA Electricial Contracting Services

Hi guys, after a design for my small electrical company, have logo design files to be incorporated into the layout, the basic concept is electrical contracting services for residential, commercial, industrial & data services, image is clean clear and strong,

Card format is to have a nice clean logo on front,with maybe the Residential – commercial – industrial - data, followed with licensed & insured, followed by contact details on backside of the card.

Target Market(s)

Residential, commercial, industrial sectors.

Industry/Entity Type

Electrical

Contact Information for Business Card

TKA logo,
Residential – commercial – industrial - data
REC: 61372
Email: tka@poralink.net.au
Phone: 0458 203 719

Requirements
Must have
• Clean & strong design.
Nice to have
• If possible, I would like the logo colours inverted so the text is orange and the background is black on the front of the card, then the backside of the card be the reverse colour
Should not have
• No Sparks, lightning bolts,

```html
<!DOCTYPE html>
<html lang="en">
<head>
<meta charset="utf-8">
<title>TKA Electrical – Business Card</title>
<link rel="stylesheet" href="https://fonts.googleapis.com/css2?family=Source+Sans+3:wght@400;600&display=swap">
<style>
  :root {
    --backdrop: #e6e6e6;
    --card-black: #0d0d0d;
    --band-white: #ecebe8;
    --brand-orange: #d9551a;
    --ink-black: #111111;
  }
  html, body {
    margin: 0;
    width: 1200px;
    height: 900px;
    overflow: hidden;
    background: var(--backdrop);
    font-family: "Source Sans 3", sans-serif;
  }
  .card-stage {
    position: relative;
    width: 1200px;
    height: 900px;
  }
  .card {
    position: absolute;
    width: 540px;
    height: 330px;
    background: var(--card-black);
    box-shadow: 0 10px 24px rgba(0,0,0,0.25);
  }
  .card--front { left: 330px; top: 90px; }
  .card--back  { left: 330px; top: 480px; }
  .card svg { display: block; width: 540px; height: 330px; }
  .band { fill: var(--band-white); }
  .rule-black { fill: var(--card-black); }
  .rule-white { fill: var(--band-white); }
  .service-label {
    fill: var(--brand-orange);
    font-size: 17px;
    letter-spacing: 1px;
    font-weight: 400;
  }
  .brand-name {
    fill: var(--brand-orange);
    font-weight: 600;
  }
  .note-text {
    fill: var(--brand-orange);
    font-size: 9.5px;
  }
  .licence-text {
    fill: var(--ink-black);
    font-size: 15px;
  }
  .contact-text {
    fill: var(--brand-orange);
    font-size: 22px;
  }
  .phone-icon { fill: var(--band-white); }
</style>
</head>
<body>
<main class="card-stage">

  <section class="card card--front" aria-label="Card front">
    <svg viewBox="0 0 540 330">
      <text class="brand-name" x="36" y="78" font-size="54">TKA</text>
      <text class="brand-name" x="38" y="96" font-size="13">Tyler Kane Electrical</text>

      <g transform="translate(0,252) rotate(-20)">
        <rect class="band" x="-30" y="-34" width="680" height="68"/>
        <rect class="rule-black" x="200" y="-27" width="460" height="5"/>
        <rect class="rule-black" x="-30" y="21" width="360" height="5"/>
        <g class="stripe-mark">
          <rect class="rule-white" x="190" y="-42" width="42" height="3"/>
          <rect class="rule-white" x="190" y="-50" width="42" height="3"/>
          <rect class="rule-white" x="190" y="-58" width="42" height="3"/>
        </g>
        <g class="stripe-mark">
          <rect class="rule-white" x="370" y="39" width="42" height="3"/>
          <rect class="rule-white" x="370" y="47" width="42" height="3"/>
          <rect class="rule-white" x="370" y="55" width="42" height="3"/>
        </g>
        <text class="service-label" x="28" y="8">RESIDENTIAL</text>
        <text class="service-label" x="160" y="8">COMMERCIAL</text>
        <text class="service-label" x="300" y="8">INDUSTRIAL</text>
        <text class="service-label" x="430" y="8">DATA</text>
      </g>

      <text class="note-text" x="508" y="268" text-anchor="end">followed with licensed &amp; insured</text>
      <text class="note-text" x="508" y="282" text-anchor="end">followed by contact details on backside of the card</text>

      <rect class="rule-white" x="0" y="304" width="540" height="3"/>
    </svg>
  </section>

  <section class="card card--back" aria-label="Card back">
    <svg viewBox="0 0 540 330">
      <g transform="translate(0,300) rotate(-20)">
        <rect class="band" x="-30" y="-150" width="700" height="88"/>
        <rect class="rule-black" x="330" y="-72" width="340" height="5"/>
        <g class="stripe-mark">
          <rect class="rule-white" x="110" y="-158" width="42" height="3"/>
          <rect class="rule-white" x="110" y="-166" width="42" height="3"/>
          <rect class="rule-white" x="110" y="-174" width="42" height="3"/>
        </g>
        <g class="stripe-mark">
          <rect class="rule-white" x="360" y="-55" width="42" height="3"/>
          <rect class="rule-white" x="360" y="-47" width="42" height="3"/>
          <rect class="rule-white" x="360" y="-39" width="42" height="3"/>
        </g>
        <text class="brand-name" x="170" y="-96" font-size="48">TKA</text>
        <text class="brand-name" x="172" y="-80" font-size="12">Tyler Kane Electrical</text>
        <text class="licence-text" x="430" y="-92">REC: 61372</text>
      </g>

      <g class="phone-icon" transform="translate(300,234)">
        <path d="M3 2 C1 4 1 8 4 12 C7 16 11 19 14 18 L16 15 L12 12 L10 14 C8 13 6 11 5 9 L7 7 L4 3 Z"/>
      </g>
      <text class="contact-text" x="510" y="252" text-anchor="end">0458 203 719</text>
      <text class="contact-text" x="510" y="282" text-anchor="end">tka@poralink.net.au</text>

      <rect class="rule-white" x="0" y="300" width="540" height="3"/>
      <rect class="rule-white" x="0" y="310" width="540" height="2"/>
    </svg>
  </section>

</main>
</body>
</html>
```